Print materials for 3-star hotel

We are changing up our print materials (notepads, letterheads, key card jackets, small flyer for the room rates) We are a 3 star business hotel in the Philippines and have mainly used grey tones and clean, simple lines. See attached photos for logo and hotel interior photos.

Target Market(s)

Business

Contact Information for Business Card

Corvina Terrace Hotel
Magistrate Lunod Avenue corner Pabilo St Cebu City 6000 Philippines
Tel: +63 32 481 7520
Mobile: +63 917 604 2893
www.corvinaterracehotel.example

Font styles to use
Serif
Sans Serif

Requirements
Must have
• Simple
• Readable font and font size
Nice to have
• Neutral colors, grey and taupes
Should not have
• No purples and bright blues

```html
<!DOCTYPE html>
<html lang="en">
<head>
<meta charset="utf-8">
<title>Corvina Terrace Hotel — Business Card</title>
<link rel="stylesheet" href="https://fonts.googleapis.com/css2?family=Open+Sans:wght@300;400;600;700&display=swap">
<style>
  :root {
    --backdrop: #d9d6d2;
    --card: #151515;
    --card-edge: #0b0b0b;
    --ink: #f2f2f2;
    --ink-soft: #bdbdbd;
    --ink-muted: #8a8a8a;
    --rule: #6b6b6b;
    --mark: #c9c9c9;
  }
  * { box-sizing: border-box; margin: 0; padding: 0; }
  html, body { width: 1200px; height: 864px; overflow: hidden; }
  body {
    background: var(--backdrop);
    font-family: "Open Sans", Arial, sans-serif;
    color: var(--ink);
    position: relative;
  }
  .card {
    position: absolute;
    left: 290px;
    width: 620px;
    height: 354px;
    background: var(--card);
    border: 1px solid var(--card-edge);
    box-shadow: 0 10px 24px rgba(0,0,0,0.25);
  }
  .card--front { top: 56px; }
  .card--back { top: 454px; }

  /* Front */
  .front-brand {
    position: absolute;
    top: 92px; left: 0; right: 0;
    text-align: center;
  }
  .brand-square {
    display: block;
    width: 46px; height: 46px;
    margin: 0 auto 18px;
    background: var(--mark);
  }
  .wordmark {
    font-weight: 300;
    color: var(--mark);
    text-transform: uppercase;
    letter-spacing: 0.32em;
    line-height: 1.35;
  }
  .front-brand .wordmark { font-size: 19px; }
  .front-web {
    position: absolute;
    top: 262px; left: 0; right: 0;
    text-align: center;
    font-size: 12px;
    letter-spacing: 0.22em;
    color: var(--ink-muted);
  }

  /* Back */
  .person {
    position: absolute;
    top: 64px; left: 40px;
  }
  .person-name {
    font-weight: 700;
    font-size: 17px;
    letter-spacing: 0.01em;
    text-transform: uppercase;
  }
  .person-title {
    font-size: 11px;
    color: var(--ink-soft);
    text-transform: uppercase;
  }
  .contact-list {
    position: absolute;
    top: 118px; left: 40px;
    list-style: none;
    font-size: 13px;
    line-height: 19px;
  }
  .contact-list li { display: flex; align-items: center; gap: 8px; }
  .contact-list svg { width: 12px; height: 12px; fill: var(--ink); flex: none; }
  .divider {
    position: absolute;
    top: 104px; left: 40px; right: 40px;
    height: 1px;
    background: var(--rule);
  }
  .back-brand {
    position: absolute;
    top: 36px; right: 40px;
    text-align: right;
    display: flex; align-items: center; gap: 14px;
  }
  .back-brand .brand-square { width: 34px; height: 34px; margin: 0; }
  .back-brand .wordmark { font-size: 14px; color: var(--ink); }
  .address {
    position: absolute;
    right: 40px; bottom: 34px;
    text-align: right;
    font-size: 14px;
    line-height: 20px;
  }
</style>
</head>
<body>

<section class="card card--front" aria-label="Business card front">
  <div class="front-brand">
    <span class="brand-square"></span>
    <p class="wordmark">Corvina Terrace<br>Hotel</p>
  </div>
  <p class="front-web">www.corvinaterracehotel.example</p>
</section>

<section class="card card--back" aria-label="Business card back">
  <div class="person">
    <p class="person-name">Marco Ilagan</p>
    <p class="person-title">President</p>
  </div>

  <div class="back-brand">
    <span class="brand-square"></span>
    <p class="wordmark">Corvina Terrace<br>Hotel</p>
  </div>

  <div class="divider"></div>

  <ul class="contact-list">
    <li>
      <svg viewBox="0 0 12 12" aria-hidden="true"><path d="M1 3.5C1 2 2.5 1 6 1s5 1 5 2.5V5H8.5V4h-5v1H1zM2.5 6h7l1 5h-9zM6 7.2a1.4 1.4 0 1 0 0 2.8 1.4 1.4 0 0 0 0-2.8z"/></svg>
      +63 32 481 7520
    </li>
    <li>
      <svg viewBox="0 0 12 12" aria-hidden="true"><path d="M3.5 0.5h5a1 1 0 0 1 1 1v9a1 1 0 0 1-1 1h-5a1 1 0 0 1-1-1v-9a1 1 0 0 1 1-1zM3.8 2v7h4.4V2zM6 9.6a.6.6 0 1 0 0 1.2.6.6 0 0 0 0-1.2z"/></svg>
      +63 917 604 2893
    </li>
    <li>
      <svg viewBox="0 0 12 12" aria-hidden="true"><path d="M3 1h6v3H3zM1 5h10v5H9V8H3v2H1zM3.6 9h4.8v2.5H3.6z"/></svg>
      +63 32 481 7521
    </li>
    <li>
      <svg viewBox="0 0 12 12" aria-hidden="true"><path d="M0.5 2.5h11v7h-11zM1.5 3.4v.4L6 6.8l4.5-3v-.4z"/></svg>
      marco@corvinaterrace.example
    </li>
  </ul>

  <p class="address">
    Magistrate Lunod Ave cor. Pabilo St<br>
    Cebu City 6000 Philippines<br>
    www.corvinaterracehotel.example
  </p>
</section>

</body>
</html>
```